GLENWICK GROOVE 2014 - Halloween Party

I need a 8.5x11 poster that can also be a jpeg for facebook and run as a display ad in print. I would like a facebook cover and profile picture that matches the poster. This is our 8th annual Halloween costume party and is our biggest event of the year.

Copy is as follows: (no particular order

8th Annual GLENWICK GROOVE
Halloween Costume Party
FRIDAY October 31st (need to emphasize date, usually I do it on Saturday.)
$400 in CASH PRIZES awarded at 9pm AND Midnight
DJ 7pm-2am in the tavern
Live music by VELVET PARROTS in the back room. 9pm.
Drink Specials, Munchies
$5 cover in advance, $10 at the door.
Birch Hollow Lodge, 4183 County Road 71, Hillsdale, NY

Target Market(s)

We are a bar and we have live music and a DJ for this party and are awarding for prizes for the best costumes (and other costumer categories.)

Industry/Entity Type

House

Font styles to use
Other font styles liked:
• halloween, spooky but readable

Requirements
Must have
• Must communicate the details clearly, be able to read from a distance. Due to the amount of Information we need to convey, I am willng to go 8x14 poster size. The emphasis should really be on "Glenwick Groove". "8th annual" is not very important and should be weighted less than Glenwick Groove.
Should not have
• shouldn't be too scary. I've had shop owners tell me that some are too scary to hang in their stores.

```html
<!DOCTYPE html>
<html lang="en">
<head>
<meta charset="utf-8">
<title>Glenwick Groove – Halloween Costume Party</title>
<link rel="stylesheet" href="https://fonts.googleapis.com/css2?family=Bangers&display=swap">
<style>
  :root {
    --night: #05070d;
    --deep-blue: #0b1a33;
    --title-blue: #1f63b0;
    --accent-blue: #2a6bb8;
    --muted-blue: #4a6891;
    --slate: #4a5362;
    --pumpkin: #f7861c;
    --pumpkin-core: #ffb640;
  }
  * { margin: 0; padding: 0; box-sizing: border-box; }
  html, body { width: 686px; height: 1200px; overflow: hidden; background: var(--night); }
  .poster {
    position: relative;
    width: 686px;
    height: 1200px;
    overflow: hidden;
    background:
      radial-gradient(ellipse 420px 140px at 540px 590px, rgba(40,110,190,0.55), transparent 70%),
      radial-gradient(ellipse 520px 300px at 300px 560px, rgba(29,79,138,0.45), transparent 75%),
      radial-gradient(ellipse 600px 500px at 340px 300px, rgba(20,45,85,0.7), transparent 80%),
      linear-gradient(180deg, #0a1426 0%, var(--deep-blue) 40%, #08101f 70%, var(--night) 100%);
  }
  .pumpkin-art {
    position: absolute;
    left: 350px;
    top: 555px;
    width: 336px;
    height: 330px;
    background:
      radial-gradient(ellipse 110px 100px at 150px 145px, var(--pumpkin-core) 0%, var(--pumpkin) 35%, #9a3d0a 70%, transparent 100%),
      radial-gradient(ellipse 170px 120px at 150px 230px, rgba(120,40,10,0.5), transparent 80%);
  }
  .copy {
    position: absolute;
    inset: 0;
    width: 686px;
    height: 1200px;
    font-family: "Bangers", "Impact", sans-serif;
    text-transform: uppercase;
  }
  .edition, .event-type { fill: var(--title-blue); }
  .event-name, .date { fill: var(--pumpkin); }
  .feature { fill: var(--accent-blue); }
  .feature.dj { fill: var(--muted-blue); }
  .feature.live { fill: var(--slate); }
  .detail { fill: var(--slate); }
  .venue { fill: var(--title-blue); }
</style>
</head>
<body>
<main class="poster">
  <div class="pumpkin-art" role="img" aria-label="Glowing jack-o'-lantern wearing headphones on autumn leaves"></div>

  <svg class="copy" viewBox="0 0 686 1200" xmlns="http://www.w3.org/2000/svg">
    <text class="edition" x="213" y="62" font-size="54" textLength="258" lengthAdjust="spacingAndGlyphs">8th Annual</text>
    <text class="event-name" x="35" y="140" font-size="88" textLength="617" lengthAdjust="spacingAndGlyphs">Glenwick Groove</text>
    <text class="event-type" x="30" y="198" font-size="64" textLength="622" lengthAdjust="spacingAndGlyphs">Halloween Costume Party</text>

    <text class="feature prizes" x="198" y="266" font-size="40" textLength="287" lengthAdjust="spacingAndGlyphs">$400 in Cash Prizes</text>
    <text class="detail prizes" x="200" y="290" font-size="24" textLength="285" lengthAdjust="spacingAndGlyphs">Awarded at 9pm and Midnight</text>

    <text class="feature dj" x="248" y="359" font-size="36" textLength="190" lengthAdjust="spacingAndGlyphs">DJ 7pm-2am</text>
    <text class="detail dj" x="248" y="387" font-size="34" textLength="190" lengthAdjust="spacingAndGlyphs">In the Tavern</text>

    <text class="feature live" x="228" y="458" font-size="40" textLength="228" lengthAdjust="spacingAndGlyphs">Live Music by</text>
    <text class="feature band" x="228" y="489" font-size="39" textLength="230" lengthAdjust="spacingAndGlyphs">Velvet Parrots</text>
    <text class="detail live" x="228" y="514" font-size="22" textLength="233" lengthAdjust="spacingAndGlyphs">In the back room, 9pm.</text>

    <text class="feature extras" x="175" y="992" font-size="37" textLength="335" lengthAdjust="spacingAndGlyphs">Drink Specials, Munchies</text>
    <text class="detail cover" x="172" y="1016" font-size="24" textLength="343" lengthAdjust="spacingAndGlyphs">$5 cover in advance, $10 at the door.</text>

    <text class="date" x="132" y="1140" font-size="63" textLength="423" lengthAdjust="spacingAndGlyphs">Friday, October 31</text>
    <text class="venue" x="35" y="1170" font-size="24" textLength="615" lengthAdjust="spacingAndGlyphs">Birch Hollow Lodge, 4183 County Road 71, Hillsdale, NY</text>
  </svg>
</main>
</body>
</html>
```